Professional IT Company Letterhead

We need a new letterhead design to incorporate our new login and business card design recently received here on Pixel Meadow. We want the same look and feel as the other two accepted projects. We want a professional and clean design.

Target Market(s)

Medical/Dental and Professional Services Businesses (CPA, Attorney, Architect etc)

Industry/Entity Type

Business

Requirements
Must have
• Clean and professional, consistent brand with our current design of our new logo and business cards.
Nice to have
• Would like to also be able to use the design on our newsletter header

```html
<!DOCTYPE html>
<html lang="en">
<head>
<meta charset="utf-8">
<title>Tidewave Letterhead</title>
<link href="https://fonts.googleapis.com/css2?family=Arimo:wght@400;700&display=swap" rel="stylesheet">
<style>
  :root {
    --brand-blue: #0877bf;
    --brand-sky: #1ea4dc;
    --paper: #ffffff;
    --footer-text: #ffffff;
    --divider: rgba(255,255,255,0.85);
  }
  html, body {
    margin: 0;
    padding: 0;
    overflow: hidden;
    background: var(--paper);
  }
  .letterhead {
    position: relative;
    width: 927px;
    height: 1200px;
    background: var(--paper);
    overflow: hidden;
    font-family: "Arimo", Arial, sans-serif;
  }
  .top-marker {
    position: absolute;
    left: 98px;
    top: 0;
  }
  .brand {
    position: absolute;
    left: 42px;
    top: 70px;
    display: flex;
    align-items: center;
    gap: 10px;
  }
  .brand-dot {
    width: 16px;
    height: 16px;
    border-radius: 50%;
    background: var(--brand-sky);
  }
  .brand-name {
    font-size: 42px;
    font-weight: 700;
    color: var(--brand-sky);
    letter-spacing: -0.5px;
    line-height: 1;
  }
  .footer-band {
    position: absolute;
    left: 0;
    top: 1085px;
    width: 927px;
    height: 115px;
    background: var(--brand-blue);
  }
  .footer-notch {
    position: absolute;
    left: 76px;
    top: 0;
  }
  .company-line {
    position: absolute;
    left: 97px;
    top: 36px;
    margin: 0;
    font-size: 15px;
    font-weight: 400;
    color: var(--footer-text);
  }
  .contact-row {
    position: absolute;
    top: 60px;
    left: 0;
    width: 100%;
    height: 16px;
    font-size: 10.8px;
    color: var(--footer-text);
  }
  .contact-item {
    position: absolute;
    top: 0;
    display: flex;
    align-items: center;
    gap: 7px;
    white-space: nowrap;
    line-height: 16px;
  }
  .contact-item svg { display: block; }
  .divider {
    position: absolute;
    top: 0;
    width: 1px;
    height: 15px;
    background: var(--divider);
  }
</style>
</head>
<body>
<div class="letterhead">
  <svg class="top-marker" width="54" height="24" viewBox="0 0 54 24" aria-hidden="true">
    <polygon points="0,0 54,0 27,24" fill="var(--brand-blue)"/>
  </svg>

  <div class="brand">
    <span class="brand-dot"></span>
    <span class="brand-name">Tidewave</span>
  </div>

  <footer class="footer-band">
    <svg class="footer-notch" width="44" height="20" viewBox="0 0 44 20" aria-hidden="true">
      <polygon points="0,0 44,0 22,20" fill="var(--paper)"/>
    </svg>

    <p class="company-line">Company Name (Pvt) Ltd.</p>

    <div class="contact-row">
      <div class="contact-item" style="left:97px">
        <svg width="8" height="12" viewBox="0 0 8 12" aria-hidden="true">
          <path d="M4 0a4 4 0 0 0-4 4c0 3 4 8 4 8s4-5 4-8a4 4 0 0 0-4-4zm0 5.6a1.6 1.6 0 1 1 0-3.2 1.6 1.6 0 0 1 0 3.2z" fill="#fff"/>
        </svg>
        <span>1204/56 Marlow Street, Seaford QLD 4100</span>
      </div>
      <span class="divider" style="left:342px"></span>

      <div class="contact-item" style="left:358px">
        <svg width="10" height="12" viewBox="0 0 10 12" aria-hidden="true">
          <path d="M2.2 0.4 3.8 2.8 2.8 4c.6 1.6 1.6 3 3 4l1.3-.9 2.2 1.8-1.3 2.2C4 10.6.6 5.6 0.8 1.6z" fill="#fff"/>
        </svg>
        <span>+11 (52) 987 654</span>
      </div>
      <span class="divider" style="left:485px"></span>

      <div class="contact-item" style="left:503px">
        <svg width="15" height="10" viewBox="0 0 15 10" aria-hidden="true">
          <rect x="0.5" y="0.5" width="14" height="9" fill="none" stroke="#fff"/>
          <path d="M0.5 0.5 7.5 6 14.5 0.5" fill="none" stroke="#fff"/>
        </svg>
        <span>hello@tidewavetech.com</span>
      </div>
      <span class="divider" style="left:666px"></span>

      <div class="contact-item" style="left:683px">
        <svg width="11" height="11" viewBox="0 0 11 11" aria-hidden="true">
          <circle cx="5.5" cy="5.5" r="5" fill="#fff"/>
          <path d="M0.5 5.5h10M5.5 0.5c-2 2.6-2 7.4 0 10M5.5 0.5c2 2.6 2 7.4 0 10" fill="none" stroke="var(--brand-blue)" stroke-width="0.8"/>
        </svg>
        <span>www.tidewavetech.com</span>
      </div>
    </div>
  </footer>
</div>
</body>
</html>
```